Flyer / Mailer for Business Debt Relief Business - Tillbrook Partners 6" x 11"

We need a 6" x 11" double sided flyer. This will be sent out to potential customers with high interest business loans. We would like the design to coordinate with the colors of our logo. I have included a mock up that we sketched out. I have also included a file of a mailer we received that we would like to use as a template (not colors or fonts, just set up). I have also included an .ai file of our logo.

```html
<!DOCTYPE html>
<html lang="en">
<head>
<meta charset="utf-8">
<title>Tillbrook Partners – Business Debt Relief Mailer</title>
<link rel="stylesheet" href="https://fonts.googleapis.com/css2?family=Questrial&family=Montserrat:wght@700;800&display=swap">
<style>
  :root {
    --navy: #143a6b;
    --blue: #0a6fc2;
    --blue-deep: #0b5cab;
    --green: #5cb531;
    --green-light: #8cc63f;
    --ink: #3c3f44;
    --grey-text: #8a8c8f;
    --paper: #ffffff;
    --panel-light: #f2f3f4;
    --panel: #e6e7e9;
  }
  * { box-sizing: border-box; margin: 0; padding: 0; }
  html, body { width: 774px; height: 1200px; overflow: hidden; }
  body { background: var(--navy); font-family: "Questrial", "Century Gothic", sans-serif; position: relative; }

  .mailer { position: absolute; left: 62px; width: 644px; box-shadow: 0 12px 14px -6px rgba(0,0,0,.45); }
  .mailer--front { top: 75px; height: 482px; background: var(--paper); }
  .mailer--back { top: 625px; height: 483px; background: var(--panel); }

  /* front photo column */
  .photo { position: absolute; left: 0; width: 171px; }
  .photo--savings { top: 0; height: 124px; background: linear-gradient(135deg, #f0ece8, #e3c3c0 55%, #c9b58a); }
  .photo--bulb { top: 124px; height: 266px; background: radial-gradient(ellipse at 50% 45%, #eef7fb, #a9d3e6 65%, #6fb2d1); }
  .photo--seedling { top: 390px; height: 92px; background: radial-gradient(ellipse at 50% 55%, #a8876a 0 18%, #f4f4f4 45%, #ffffff); }

  .band { position: absolute; left: 171px; display: flex; align-items: center; justify-content: center; text-align: center; color: #fff; }
  .band--tagline { top: 0; width: 301px; height: 57px; background: linear-gradient(90deg, var(--green-light), var(--green)); font-size: 13px; }
  .band--intro { top: 57px; width: 301px; height: 67px; background: var(--blue); font-size: 12.6px; line-height: 1.25; padding: 0 10px; }
  .band--question { top: 124px; width: 473px; height: 32px; background: linear-gradient(90deg, var(--green), var(--green-light)); justify-content: flex-start; padding-left: 15px; font-family: "Montserrat", sans-serif; font-weight: 700; font-size: 12.5px; }
  .band--website { top: 390px; width: 473px; height: 34px; background: linear-gradient(90deg, var(--green), var(--green-light)); font-size: 15.5px; }
  .band--website strong { font-family: "Montserrat", sans-serif; font-weight: 700; margin-left: 5px; }
  .band--contact { top: 424px; width: 473px; height: 58px; background: linear-gradient(90deg, var(--blue-deep), var(--blue)); flex-direction: column; font-size: 13.4px; gap: 4px; }
  .contact-row { display: flex; gap: 22px; align-items: center; }
  .contact-row span { display: flex; align-items: center; gap: 6px; }

  .brand { position: absolute; top: 0; left: 472px; width: 172px; height: 124px; display: flex; align-items: center; justify-content: center; gap: 7px; }
  .brand__square { width: 12px; height: 12px; background: var(--green); }
  .brand__name { font-size: 13px; letter-spacing: .5px; color: var(--ink); text-transform: uppercase; }

  .help { position: absolute; top: 156px; left: 171px; width: 473px; height: 234px; background: linear-gradient(90deg, #f4f6f9, #e7edf5 60%, #d8e3ef); overflow: hidden; }
  .help__title { position: absolute; top: 13px; left: 15px; font-family: "Montserrat", sans-serif; font-weight: 800; font-size: 16px; color: var(--ink); }
  .help__list { position: absolute; top: 40px; left: 12px; list-style: none; font-size: 11.6px; color: var(--ink); }
  .help__list li { height: 19.2px; display: flex; align-items: center; gap: 8px; }
  .help__list li::before { content: ""; width: 5px; height: 5px; border: 1.3px solid var(--ink); transform: rotate(45deg); }
  .photo--consultant { position: absolute; top: 9px; left: 267px; width: 206px; height: 225px; background: linear-gradient(160deg, rgba(255,255,255,0), #c9d5e2 40%, #2c3648 75%); }

  /* back */
  .back-light { position: absolute; inset: 0; }
  .back-panel { position: absolute; top: 0; left: 25px; width: 242px; height: 326px; background: var(--blue); color: #fff; text-align: center; }
  .back-panel .brand__name { color: #fff; font-size: 14px; }
  .back-brand { height: 100px; display: flex; align-items: center; justify-content: center; gap: 7px; padding-top: 14px; }
  .back-brand .brand__square { background: #fff; }
  .back-block { margin: 0 35px; padding: 6px 0; border-top: 1px dashed rgba(255,255,255,.8); font-size: 13.4px; line-height: 1.2; }
  .back-block:first-of-type { margin-top: 8px; }
  .back-block--address { padding-bottom: 8px; }
  .back-block--slogan { padding: 10px 0 12px; }
  .back-block--pitch { margin: 0 0; padding: 10px 30px 0; border-top-color: transparent; background-image: linear-gradient(90deg, rgba(255,255,255,.8) 50%, transparent 50%); background-size: 6px 1px; background-repeat: repeat-x; background-position: 35px 0; background-clip: border-box; }
  .back-block--pitch { margin: 0 35px; padding: 10px 0 0; border-top: 1px dashed rgba(255,255,255,.8); background: none; }
  .back-block--pitch p { margin: 0 -10px; }

  .postage { position: absolute; top: 33px; left: 494px; width: 104px; height: 120px; border: 1.5px solid #a2a4a7; display: flex; align-items: center; justify-content: center; text-align: center; color: var(--grey-text); font-size: 15px; line-height: 1.25; }
  .area-label { position: absolute; color: var(--grey-text); font-size: 15.5px; transform: translate(-50%, -50%); white-space: nowrap; }
</style>
</head>
<body>

<section class="mailer mailer--front">
  <div class="photo photo--savings" role="img" aria-label="Photo of a pink piggy bank beside stacks of coins"></div>
  <div class="photo photo--bulb" role="img" aria-label="Photo of a hand dropping a coin into a light bulb filled with coins"></div>
  <div class="photo photo--seedling" role="img" aria-label="Photo of cupped hands holding soil with a small green seedling"></div>

  <div class="band band--tagline">Helping Business Focus on What Matters!</div>
  <div class="band band--intro">We Understand That Merchant Cash Advance Loans Can Be A Burden On Your Business</div>

  <div class="brand">
    <span class="brand__square"></span>
    <span class="brand__name">Tillbrook Partners</span>
  </div>

  <div class="band band--question">Overwhelmed by daily/Weekly Payment?</div>

  <div class="help">
    <div class="photo--consultant" role="img" aria-label="Photo of a smiling consultant in a suit holding a laptop"></div>
    <h2 class="help__title">WE CAN HELP!</h2>
    <ul class="help__list">
      <li>This is not loan, WE ARE NOT LENDERS!</li>
      <li>Improve Your Business Cash Flow Immediately</li>
      <li>Move Payment To On Monthly Amount</li>
      <li>Reduce The Amount You'are Paying Out Monthly</li>
      <li>Strategic Alternatives To His Interest Loans</li>
      <li>Fast, Confidential Business Debt Relief</li>
      <li>No-obligation Consultation</li>
      <li>Absolutely No Credit Pulls</li>
      <li>No Collateral, No Financials</li>
    </ul>
  </div>

  <div class="band band--website">Visit our website: <strong>www.tillbrookrelief.com</strong></div>
  <div class="band band--contact">
    <div>CALL NOW FOR FREE CONSULTATION WITH OUR EXPERTS</div>
    <div class="contact-row">
      <span>
        <svg width="16" height="16" viewBox="0 0 24 24" fill="#fff" aria-hidden="true"><path d="M6.6 10.8a15.1 15.1 0 0 0 6.6 6.6l2.2-2.2a1 1 0 0 1 1-.25 11.4 11.4 0 0 0 3.6.57 1 1 0 0 1 1 1V20a1 1 0 0 1-1 1A17 17 0 0 1 3 4a1 1 0 0 1 1-1h3.5a1 1 0 0 1 1 1c0 1.25.2 2.45.57 3.6a1 1 0 0 1-.25 1z"/></svg>
        (844) 555-0172
      </span>
      <span>
        <svg width="18" height="14" viewBox="0 0 24 18" fill="#fff" aria-hidden="true"><path d="M1 1h22v16H1z" fill="none" stroke="#fff" stroke-width="2"/><path d="M1 1l11 8 11-8" fill="none" stroke="#fff" stroke-width="2"/></svg>
        info@tillbrookrelief.com
      </span>
    </div>
  </div>
</section>

<section class="mailer mailer--back">
  <svg class="back-light" width="644" height="483" aria-hidden="true">
    <polygon points="0,0 437,0 437,175 354,175 354,338 0,338" fill="var(--panel-light)"/>
  </svg>

  <div class="back-panel">
    <div class="back-brand">
      <span class="brand__square"></span>
      <span class="brand__name">Tillbrook Partners</span>
    </div>
    <div class="back-block back-block--address">1450 W. Harlan Ave<br>Denton, TX 76201</div>
    <div class="back-block back-block--slogan">Strategic Debt Relief For<br>Business of all Sizes</div>
    <div class="back-block back-block--pitch"><p>Stop Taking Out Loans To Pay Off Other Loans. Take Back Your Business Cash Flow And Focus On What Matters.</p></div>
  </div>

  <div class="postage">Postage<br>Area</div>
  <div class="area-label" style="left:482px;top:251px;">Address Area</div>
  <div class="area-label" style="left:315px;top:408px;">Barcode Area</div>
</section>

</body>
</html>
```